Gourmet Restaurant Coffee Cup Print Design

We would like to redesign our coffee cup for our restaurant chain. Please visit our website at: www.dorvanti.ca.

Disposable Cup should be bilingual in English and French. We will provide translations. One side is to be french and the other English.

I have uploaded also the files that were provided to us by the cup manufacturer. These templates have all the necessary instructions.

Target Market(s)

Business Professionals, Millenials

Industry/Entity Type

Restaurant

Font styles to use
Serif
Sans Serif
Script

Requirements
Must have
• our entire logo or only the "DORVANTI'S" word in the logo.
• We are looking for 4 cup sizes with the same design but maybe a distinguishing color in each size of cup.
• We can provide cup templates in PDF along with full manufacturer instructions.
• We're looking for a simple clean design with a predominantly white background. The lid of the cup is white.
Nice to have
• Our motto or tag line is:
• A world of taste
Should not have
• photos only use illustrations

```html
<!DOCTYPE html>
<html lang="en">
<head>
<meta charset="utf-8">
<title>Dorvanti's Cup Wrap – Print Layout</title>
<link rel="stylesheet" href="https://fonts.googleapis.com/css2?family=Montserrat:wght@500;700&family=Open+Sans:wght@700&display=swap">
<style>
  :root {
    --brand-green: #1e6459;
    --paper: #ffffff;
    --frame-line: #8a8a8a;
    --guide-line: #9a9a9a;
    --label-ink: #111111;
  }
  html, body {
    margin: 0;
    padding: 0;
    width: 1200px;
    height: 876px;
    overflow: hidden;
    background: var(--paper);
  }
  .cup-sheet {
    display: block;
    width: 1200px;
    height: 876px;
  }
  .sheet-frame, .print-frame {
    fill: none;
    stroke: var(--frame-line);
    stroke-width: 1;
  }
  .bleed-guide {
    fill: none;
    stroke: var(--guide-line);
    stroke-width: 1;
    stroke-dasharray: 6 4;
  }
  .trim-line {
    stroke: var(--frame-line);
    stroke-width: 1;
  }
  .brand-band { fill: var(--brand-green); }
  .brand-name {
    font-family: "Montserrat", sans-serif;
    font-weight: 700;
    font-size: 19px;
    letter-spacing: 1px;
    fill: var(--paper);
  }
  .tagline {
    font-family: "Montserrat", sans-serif;
    font-weight: 500;
    font-size: 12px;
    letter-spacing: 1.6px;
    fill: var(--brand-green);
  }
  .tagline-rule {
    stroke: var(--brand-green);
    stroke-width: 0.8;
    fill: none;
  }
  .tagline-notch {
    fill: var(--paper);
    stroke: var(--brand-green);
    stroke-width: 0.8;
  }
  .swatch { fill: var(--brand-green); }
  .swatch-label {
    font-family: "Open Sans", sans-serif;
    font-weight: 700;
    font-size: 15px;
    fill: var(--label-ink);
  }
</style>
</head>
<body>
<svg class="cup-sheet" viewBox="0 0 1200 876" xmlns="http://www.w3.org/2000/svg">
  <defs>
    <clipPath id="wrap-area">
      <rect x="174" y="202" width="931" height="459"/>
    </clipPath>
    <g id="notches-top-bottom">
      <path class="tagline-notch" d="M-4 0 L0 -4 L4 0 Z"/>
      <path class="tagline-notch" d="M-4 31 L0 35 L4 31 Z"/>
    </g>
  </defs>

  <!-- sheet and print frames -->
  <rect class="sheet-frame" x="121" y="148" width="1040" height="565"/>
  <rect class="print-frame" x="174" y="202" width="931" height="459"/>
  <rect class="bleed-guide" x="182" y="227" width="915" height="427"/>
  <line class="trim-line" x1="182" y1="238" x2="1097" y2="238"/>

  <!-- brand bands -->
  <rect class="brand-band" x="314" y="227" width="188" height="427"/>
  <text class="brand-name" x="408" y="419" text-anchor="middle">DORVANTI'S</text>

  <rect class="brand-band" x="781" y="227" width="188" height="427"/>
  <text class="brand-name" x="875" y="419" text-anchor="middle">DORVANTI'S</text>

  <!-- English tagline -->
  <g class="tagline-block">
    <line class="tagline-rule" x1="567" y1="397" x2="710" y2="397"/>
    <line class="tagline-rule" x1="567" y1="428" x2="710" y2="428"/>
    <use href="#notches-top-bottom" x="638.5" y="397"/>
    <text class="tagline" x="567" y="417" textLength="143" lengthAdjust="spacingAndGlyphs">A WORLD OF TASTE</text>
  </g>

  <!-- French tagline, wrapping across the seam -->
  <g class="tagline-block" clip-path="url(#wrap-area)">
    <line class="tagline-rule" x1="174" y1="397" x2="262" y2="397"/>
    <line class="tagline-rule" x1="174" y1="428" x2="262" y2="428"/>
    <use href="#notches-top-bottom" x="188" y="397"/>
    <text class="tagline" x="262" y="417" text-anchor="end">UN MONDE DE GOÛT</text>

    <line class="tagline-rule" x1="1019" y1="397" x2="1105" y2="397"/>
    <line class="tagline-rule" x1="1019" y1="428" x2="1105" y2="428"/>
    <use href="#notches-top-bottom" x="1094" y="397"/>
    <text class="tagline" x="1019" y="417">UN MONDE DE GOÛT</text>
  </g>

  <!-- colour reference -->
  <rect class="swatch" x="862" y="760" width="33" height="33"/>
  <text class="swatch-label" x="909" y="784">Pantone 342 U</text>
</svg>
</body>
</html>
```